IT services web page design

Hello!

We need new design for our web site, obviously :)

Our company is service oriented and we are maintaining, configuring and fixing problems for IT + selling other internet related services.

Our speciality are in area of internet services (web, dns, email, databases, backup...) and internet servers technology.

We also provide service and sales of Zentor Apps and Halvorix Quorvo365 for which we are certified by Zentor and Halvorix.

Other services that we provide (not so in focus) are: VPS hosting, remote backup, web hosting, vexalink fixing...

People mostly call us when they have a problems and this is core idea that new web site has to communicate - We can fix your server / web / email problems, save your money and as* :)

Our team have 15+ years experience with all range of internet technology + bunch of certificates from Halvorix and Tandix [we need to show people we have certificates].
Our qualities: experience, knowledge, delivery on time

In start we will not have blog section, but we need it in future. We also need place for plonkit feeds on web site.

Depth of the site should be max. level 2.

This site will go out in two languages so we need switch button on page from pone language to another.

Target Market(s)

small and mid size business that use internet services for daily operations and main business

Industry/Entity Type

Internet

Requirements
Must have
• * design should be in the way that responsive web could be made

Nice to have
• Long format will be OK for us. Like today pages that list all services and benefits on one loooong web page...

Logo is in attachment. It will be nice to have it on web site but if you find it not appropriate you can change it or put another one.

```html
<!DOCTYPE html>
<html lang="hr">
<head>
<meta charset="utf-8">
<title>Meridon grupa – Virtual Private Server</title>
<link rel="stylesheet" href="https://fonts.googleapis.com/css2?family=Source+Sans+3:wght@400;600&family=Arimo:wght@400;700&display=swap">
<style>
  :root {
    --page-bg: #ffffff;
    --side-blue: #86a3cc;
    --nav-top: #a7b4b3;
    --nav-bottom: #879796;
    --nav-text: #ffffff;
    --crumb: #9a9ae0;
    --rule: #444444;
    --title-panel: #e8e8fa;
    --title-text: #5858cc;
    --accent-red: #7a2c2c;
    --body-text: #585858;
    --news-panel: #e7e7f8;
    --news-title: #8a8ade;
    --news-text: #b2b2d2;
    --logo-text: #111111;
    --logo-dot: #3f8fc0;
  }
  * { box-sizing: border-box; margin: 0; padding: 0; }
  html, body { width: 1200px; height: 1000px; overflow: hidden; background: var(--page-bg); }
  .page { position: relative; width: 1200px; height: 1000px; font-family: "Source Sans 3", sans-serif; overflow: hidden; }

  .header-photo {
    position: absolute; left: 0; top: 0; width: 1036px; height: 386px;
    background: linear-gradient(100deg, #3a2a8a 0%, #6a3a9a 22%, #b0503a 42%, #d8703a 55%, #5a3a2a 68%, #2f3a1e 82%, #3a4a22 100%);
  }
  .header-side { position: absolute; left: 1040px; top: 0; width: 160px; height: 386px; background: var(--side-blue); }

  .main-nav {
    position: absolute; left: 0; top: 390px; width: 1200px; height: 36px;
    background: linear-gradient(var(--nav-top), var(--nav-bottom));
    font-family: "Arimo", sans-serif; font-size: 24px; color: var(--nav-text);
  }
  .main-nav a { color: inherit; text-decoration: none; position: absolute; top: 2px; }
  .main-nav .current::before {
    content: ""; position: absolute; left: -14px; top: 10px;
    border-left: 7px solid #7a1a1a; border-top: 5px solid transparent; border-bottom: 5px solid transparent;
  }

  .brand-name {
    position: absolute; left: 696px; top: 322px;
    font-family: "Arimo", sans-serif; font-weight: 700; font-size: 46px;
    color: var(--logo-text); letter-spacing: 1px; line-height: 1; white-space: nowrap;
  }
  .brand-dot { position: absolute; left: 1068px; top: 282px; width: 118px; height: 118px; border-radius: 50%; background: var(--logo-dot); }

  .breadcrumb {
    position: absolute; left: 28px; top: 446px; width: 662px; height: 22px;
    border-bottom: 1px solid var(--rule);
    font-size: 18px; font-weight: 600; color: var(--crumb); line-height: 22px;
  }

  .title-panel { position: absolute; left: 28px; top: 485px; width: 664px; height: 108px; background: var(--title-panel); }
  .title-panel h1 { position: absolute; right: 16px; top: 32px; font-size: 40px; font-weight: 400; color: var(--title-text); line-height: 1.2; }
  .title-bar { position: absolute; left: 28px; top: 592px; width: 664px; height: 14px; background: linear-gradient(var(--accent-red), #b08888 70%, #ffffff); }

  .article { position: absolute; left: 28px; top: 630px; width: 660px; font-size: 23px; line-height: 30px; color: var(--body-text); white-space: nowrap; }
  .article p { margin-bottom: 30px; }
  .article .drop { font-size: 42px; line-height: 20px; }

  .news { position: absolute; left: 763px; top: 493px; width: 414px; height: 507px; background: var(--news-panel); }
  .news h2 { position: absolute; left: 17px; top: 32px; font-size: 40px; font-weight: 400; color: var(--news-title); line-height: 1; }
  .news-rule { position: absolute; left: 780px; top: 566px; width: 420px; height: 3px; background: var(--accent-red); }
  .news-list { position: absolute; left: 17px; top: 75px; width: 400px; font-size: 23px; line-height: 30px; color: var(--news-text); list-style: none; white-space: nowrap; }
  .news-list li { margin-bottom: 30px; }
</style>
</head>
<body>
<div class="page">
  <div class="header-photo" role="img" aria-label="Close-up photo of a circuit board with a chip and ribbon cable under a purple grid overlay"></div>
  <div class="header-side"></div>

  <nav class="main-nav">
    <a style="left:27px">Home</a>
    <a class="current" style="left:132px">VPS</a>
    <a style="left:235px">CMMS</a>
    <a style="left:359px">Apps</a>
    <a style="left:462px">Hosting</a>
    <a style="left:593px">Contact</a>
  </nav>

  <div class="brand-dot"></div>
  <div class="brand-name">Meridon grupa</div>

  <div class="breadcrumb">&gt;VPS&gt; Virtual Private Server</div>

  <div class="title-panel"><h1>Virtual Private Server</h1></div>
  <div class="title-bar"></div>

  <div class="article">
    <p><span class="drop">R</span>azvijate li napredne web stranice i aplikacije ili vodite<br>web studio koji svojim klijentima pruža kompletnu uslugu<br>uključujući i web hosting, tada je VPS je odlično rješenje.</p>
    <p>Virtual Private Server (VPS) je virtualna instanca server soft-<br>warea i hardwarea koja omogućuje brzo i jednostavno ska-<br>liranje potrebnih resursa za aplikacije i ostale zadaće.</p>
    <p>Meridon grupa d.o.o. osigurava i konfigurira VPS-ove prema<br>korisničkim zahtjevima i potrebama te osigurava uslugu<br>održavanja i podrške nesmetanom radu VPS-a.</p>
    <p>VPS 1</p>
  </div>

  <aside class="news">
    <h2>Novosti</h2>
    <ul class="news-list">
      <li>Meridon – zentor apps autorizian</li>
      <li>Quellix autoriziran</li>
      <li>Problemi s internetom?<br>Ako Vam je web site (stranica)<br>nedostupna ili hakirana, VPS vrlo spor<br>ili niste u mogućnosti primati email<br>poruke zbog kvara na serveru, nazo-<br>vite +385 91 4410 238 bez obzira bili<br>naš klijent ili ne.</li>
      <li>Napravit ćemo detekciju kvara i u vrlo<br>kratkom roku riješiti problem.</li>
    </ul>
  </aside>
  <div class="news-rule"></div>
</div>
</body>
</html>
```